Network Video Recorder Sticker

I need a sticker design for a network video recorder (NVR) metal box. It will be on the front cover and will identify my product. The NVR is to be used on boats and record the fishing activities. My company name is TideOptic HD Systems. I prefer a combination of Blue Water color and gray or any other nice combination. My idea is to have something flat and minimalist like an eye with a lens inside and some kind of lines simulating the waves of the sea. Any other idea is welcome. Dimensions file included on Adobe Ilustrator.

Target Market(s)

Marine and fishing vessels

Industry/Entity Type

Product

Colors
0292cd
0555a3
3176b5

Requirements
Nice to have
• minimalist flat waves like desing with some kind of lens like inside a silluotee of a eye. Please note It will the front cover for a network video Recorder uses in Fishing Boats.

```html
<!DOCTYPE html>
<html lang="en">
<head>
<meta charset="utf-8">
<title>TideOptic HD Systems – NVR Front Sticker</title>
<link rel="stylesheet" href="https://fonts.googleapis.com/css2?family=Saira+Condensed:wght@500;600&display=swap">
<style>
  :root {
    --stage-center: #282828;
    --stage-edge: #131313;
    --paper: #ffffff;
    --deep-blue: #0c4fa2;
    --mid-blue: #1a8fd0;
    --light-blue: #1b96d2;
    --bright-blue: #00b4ea;
    --ink-deep: #0a4a9e;
    --ink-light: #1a8fd0;
  }
  * { margin: 0; padding: 0; box-sizing: border-box; }
  html, body { width: 1200px; height: 1000px; overflow: hidden; }
  body {
    position: relative;
    background: radial-gradient(ellipse at center, var(--stage-center) 0%, var(--stage-edge) 75%);
    font-family: "Saira Condensed", "Arial Narrow", sans-serif;
  }
  .sticker {
    position: absolute;
    left: 106px;
    width: 987px;
    height: 239px;
    background: var(--paper);
    overflow: hidden;
  }
  .sticker--classic { top: 184px; --ink: var(--ink-deep); --brand-ink: var(--ink-deep); }
  .sticker--gradient { top: 584px; --ink: var(--ink-light); --brand-ink: var(--paper); }
  .sticker__waves { position: absolute; inset: 0; width: 987px; height: 239px; }
  .sticker__motif {
    position: absolute;
    left: 250px; top: 44px;
    width: 190px; height: 88px;
    border-radius: 44px;
    background: radial-gradient(ellipse at center, rgba(26,143,208,0.55), rgba(26,143,208,0.12) 70%, rgba(26,143,208,0) 100%);
  }
  .sticker__product {
    position: absolute;
    left: 651px; top: 14px;
    font-size: 31px; font-weight: 500;
    letter-spacing: -0.3px;
    color: var(--ink);
    white-space: nowrap;
  }
  .indicator {
    position: absolute;
    top: 132px;
    font-size: 27px; font-weight: 600;
    color: var(--ink);
    text-align: center;
  }
  .indicator--disk { left: 758px; }
  .indicator--power { left: 821px; }
  .indicator__icon { display: block; margin: 6px auto 0; width: 16px; height: 16px; }
  .sticker__brand {
    position: absolute;
    left: 39px; top: 197px;
    font-size: 25px; font-weight: 600;
    letter-spacing: 0.5px;
    color: var(--brand-ink);
    white-space: nowrap;
  }
</style>
</head>
<body>

<section class="sticker sticker--classic">
  <svg class="sticker__waves" viewBox="0 0 987 239" aria-hidden="true">
    <path d="M0,104 C120,90 250,100 380,150 C520,200 750,218 987,219 V239 H0 Z" fill="var(--deep-blue)"/>
    <path d="M0,239 C20,180 60,158 150,156 C350,156 600,200 987,229 V239 Z" fill="var(--light-blue)"/>
  </svg>
  <div class="sticker__motif" role="img" aria-label="Small school of outlined fish with bubbles"></div>
  <p class="sticker__product">Network video Recorder</p>
  <div class="indicator indicator--disk">Disk
    <svg class="indicator__icon" viewBox="0 0 16 16" aria-hidden="true"><circle cx="8" cy="8" r="6" fill="none" stroke="currentColor" stroke-width="2.2"/><circle cx="8" cy="8" r="2.2" fill="currentColor"/></svg>
  </div>
  <div class="indicator indicator--power">Power
    <svg class="indicator__icon" viewBox="0 0 16 16" aria-hidden="true"><path d="M4.8,4.5 A5,5 0 1 0 11.2,4.5" fill="none" stroke="currentColor" stroke-width="2" stroke-linecap="round"/><line x1="8" y1="2" x2="8" y2="8" stroke="currentColor" stroke-width="2" stroke-linecap="round"/></svg>
  </div>
  <p class="sticker__brand">TideOptic HD Systems</p>
</section>

<section class="sticker sticker--gradient">
  <svg class="sticker__waves" viewBox="0 0 987 239" aria-hidden="true">
    <defs>
      <linearGradient id="deepWave" x1="0" y1="0" x2="0" y2="1">
        <stop offset="0" stop-color="#0c4fa2"/>
        <stop offset="1" stop-color="#0a8fd0"/>
      </linearGradient>
      <linearGradient id="lightWave" x1="0" y1="0" x2="0" y2="1">
        <stop offset="0" stop-color="#1b96d2"/>
        <stop offset="1" stop-color="#00b4ea"/>
      </linearGradient>
    </defs>
    <path d="M0,104 C120,90 250,100 380,150 C520,200 750,218 987,219 V239 H0 Z" fill="url(#deepWave)"/>
    <path d="M0,239 C20,180 60,158 150,156 C350,156 600,200 987,229 V239 Z" fill="url(#lightWave)"/>
  </svg>
  <div class="sticker__motif" role="img" aria-label="Small school of outlined fish with bubbles"></div>
  <p class="sticker__product">Network video Recorder</p>
  <div class="indicator indicator--disk">Disk
    <svg class="indicator__icon" viewBox="0 0 16 16" aria-hidden="true"><circle cx="8" cy="8" r="6" fill="none" stroke="currentColor" stroke-width="2.2"/><circle cx="8" cy="8" r="2.2" fill="currentColor"/></svg>
  </div>
  <div class="indicator indicator--power">Power
    <svg class="indicator__icon" viewBox="0 0 16 16" aria-hidden="true"><path d="M4.8,4.5 A5,5 0 1 0 11.2,4.5" fill="none" stroke="currentColor" stroke-width="2" stroke-linecap="round"/><line x1="8" y1="2" x2="8" y2="8" stroke="currentColor" stroke-width="2" stroke-linecap="round"/></svg>
  </div>
  <p class="sticker__brand">TideOptic HD Systems</p>
</section>

</body>
</html>
```